Business Card Design Project

I would like a business card created for a new company. This is a holding company that acts as my investment company. It holds real estate and service based companies. The name of the company is Lucernaria which is Italian for Lanternry. Defined as development or growth.
We currently have no logo. I really like some of the "different" cards out there. Potentially metallic or grey/black. That looks premium/hi-end and unique. I am not sure if your design would be specific to the card stock I end with our just logo/design/font.
Real Estate

```html
<!DOCTYPE html>
<html lang="en">
<head>
<meta charset="utf-8">
<title>Lucernaria — Business Card</title>
<link href="https://fonts.googleapis.com/css2?family=Jost:wght@300;400&display=swap" rel="stylesheet">
<style>
  :root {
    --page: #ffffff;
    --card-dark: #151718;
    --card-mid: #474e50;
    --card-light: #8a9293;
    --glow: rgba(225, 228, 226, 0.55);
    --glow-soft: rgba(200, 205, 204, 0.28);
    --text-main: #ffffff;
    --text-soft: #dfe2e2;
    --text-muted: #c4c9c9;
  }
  * { margin: 0; padding: 0; box-sizing: border-box; }
  html, body {
    width: 1200px; height: 846px; overflow: hidden;
    background: var(--page);
    font-family: "Jost", "Futura", sans-serif;
  }
  .canvas { position: relative; width: 1200px; height: 846px; }

  .card {
    position: absolute;
    width: 486px; height: 314px;
    overflow: hidden;
    box-shadow: 6px 6px 10px rgba(0,0,0,0.35);
  }
  .card--front {
    left: 84px; top: 77px;
    background: radial-gradient(ellipse at 50% 45%, var(--card-light) 0%, var(--card-mid) 50%, var(--card-dark) 100%);
  }
  .card--back {
    left: 619px; top: 449px;
    background: radial-gradient(ellipse at 40% 30%, var(--card-light) 0%, var(--card-mid) 42%, var(--card-dark) 95%);
  }

  .card__art { position: absolute; inset: 0; }
  .card--front .card__art {
    background:
      radial-gradient(ellipse 42% 60% at 58% 45%, var(--glow) 0%, transparent 100%),
      linear-gradient(90deg, var(--glow-soft) 0%, transparent 85%);
  }
  .card--back .card__art {
    top: 104px; bottom: 60px; right: 150px;
    background: linear-gradient(90deg, transparent 0%, var(--glow-soft) 45%, var(--glow) 100%);
    -webkit-mask-image: linear-gradient(90deg, #000 70%, transparent 100%);
            mask-image: linear-gradient(90deg, #000 70%, transparent 100%);
  }

  .brand { position: absolute; color: var(--text-main); }
  .brand__name { font-weight: 400; line-height: 1; }
  .brand__slogan { font-weight: 300; color: var(--text-muted); line-height: 1; }

  .card--front .brand { left: 57px; top: 134px; }
  .card--front .brand__name { font-size: 60px; letter-spacing: 0.04em; }
  .card--front .brand__slogan { font-size: 26px; letter-spacing: 0.1em; margin-top: 6px; }

  .card--back .brand { left: 31px; top: 30px; }
  .card--back .brand__name { font-size: 28px; letter-spacing: 0.05em; }
  .card--back .brand__slogan { font-size: 12px; letter-spacing: 0.06em; margin-top: 2px; }

  .contact {
    position: absolute; right: 33px; top: 30px;
    text-align: right; color: var(--text-soft);
    font-weight: 300; font-size: 16px; line-height: 18px;
    letter-spacing: 0.03em;
  }
  .contact__name { font-size: 19px; line-height: 20px; font-weight: 400; color: var(--text-main); }
  .contact__role { font-size: 17px; }
  .contact__group { margin-top: 8px; }
  .contact__group:first-of-type { margin-top: 12px; }
  .contact__label { font-weight: 400; color: var(--text-main); }
</style>
</head>
<body>
<main class="canvas">

  <section class="card card--front" aria-label="Business card front">
    <div class="card__art" role="img" aria-label="Dark concrete texture with large light arrow motif"></div>
    <div class="brand">
      <div class="brand__name">LUCERNARIA</div>
      <div class="brand__slogan">your holding company slogan</div>
    </div>
  </section>

  <section class="card card--back" aria-label="Business card back">
    <div class="card__art" role="img" aria-label="Concrete texture with a row of light arrow motifs"></div>
    <div class="brand">
      <div class="brand__name">LUCERNARIA</div>
      <div class="brand__slogan">your holding company slogan</div>
    </div>
    <div class="contact">
      <div class="contact__name">NAME NAME</div>
      <div class="contact__role">what you do</div>
      <div class="contact__group">
        <div class="contact__label">telephone</div>
        <div class="contact__value">0000 000 000 000</div>
      </div>
      <div class="contact__group">
        <div class="contact__label">address</div>
        <div class="contact__value">this is your street</div>
        <div class="contact__value">this is your street</div>
      </div>
      <div class="contact__group">
        <div class="contact__label">email</div>
        <div class="contact__value">this is your email</div>
      </div>
      <div class="contact__group">
        <div class="contact__label">website</div>
        <div class="contact__value">this is your site</div>
      </div>
    </div>
  </section>

</main>
</body>
</html>
```